The Larchmont Fitters

We need a business card design for our wardrobe company.
Please visit our website www.glimmerbayinteriors.com to get an idea of who we are.

```html
<!DOCTYPE html>
<html lang="en">
<head>
<meta charset="utf-8">
<title>The Larchmont Fitters — Business Card</title>
<link href="https://fonts.googleapis.com/css2?family=Lato:wght@400;700&display=swap" rel="stylesheet">
<style>
  :root {
    --stage: #d6d6d6;
    --card-light: #f5f5f5;
    --card-dark: #2b2828;
    --ink: #1e1c1c;
    --ink-soft: #3a3838;
    --band: #231f20;
    --white: #ffffff;
    --muted-on-dark: #8a8686;
  }
  * { box-sizing: border-box; margin: 0; padding: 0; }
  html, body { width: 1200px; height: 873px; overflow: hidden; }
  body {
    background: var(--stage);
    font-family: "Lato", sans-serif;
    color: var(--ink);
    display: flex;
    align-items: center;
    justify-content: center;
    gap: 50px;
  }
  .card {
    position: relative;
    width: 540px;
    height: 308px;
    box-shadow: 0 4px 14px rgba(0,0,0,0.18);
  }
  .card-front { background: var(--card-light); }
  .card-back { background: var(--card-dark); }

  /* Front */
  .name-band {
    position: absolute;
    left: 0; top: 54px;
    width: 250px; height: 32px;
    background: var(--band);
    color: var(--white);
    padding: 3px 0 0 47px;
  }
  .person-name { font-size: 15px; font-weight: 700; line-height: 1.1; }
  .person-role { font-size: 11px; font-weight: 400; line-height: 1.2; }
  .brand-front {
    position: absolute;
    left: 262px; top: 56px;
    display: flex; align-items: center; gap: 10px;
  }
  .brand-mark {
    width: 28px; height: 28px;
    border: 2px solid var(--ink);
  }
  .brand-text { line-height: 1.35; }
  .brand-name {
    font-size: 11.5px; font-weight: 700;
    letter-spacing: 0.4px; text-transform: uppercase;
  }
  .brand-tagline { font-size: 10.5px; font-weight: 700; }
  .address {
    position: absolute;
    left: 47px; top: 180px;
    font-size: 11px; line-height: 1.35;
    font-style: normal;
    color: var(--ink-soft);
  }
  .contacts {
    position: absolute;
    left: 47px; top: 222px;
    list-style: none;
    font-size: 11px; line-height: 1.4;
    color: var(--ink-soft);
  }
  .contacts li { display: flex; align-items: center; gap: 5px; }
  .contacts svg { width: 9px; height: 9px; fill: none; stroke: var(--ink-soft); stroke-width: 1.4; }

  /* Back */
  .brand-back {
    position: absolute;
    left: 0; right: 0; top: 120px;
    display: flex; justify-content: center; align-items: center; gap: 14px;
  }
  .brand-back .brand-mark {
    width: 42px; height: 42px;
    border-color: #1d1a1a;
    box-shadow: 0 1px 0 rgba(255,255,255,0.08);
  }
  .brand-back .brand-text { color: var(--muted-on-dark); line-height: 1.5; }
  .brand-back .brand-name { font-size: 14px; font-weight: 400; letter-spacing: 0.8px; }
  .brand-back .brand-tagline { font-size: 13.5px; font-weight: 400; text-align: center; }
  .back-url {
    position: absolute;
    left: 0; right: 0; top: 251px;
    text-align: center;
    font-size: 10.5px;
    color: var(--white);
  }
  .back-url strong { font-weight: 700; }
</style>
</head>
<body>
  <section class="card card-front" aria-label="Card front">
    <div class="name-band">
      <p class="person-name">Martin Ellery</p>
      <p class="person-role">Managing Director</p>
    </div>
    <div class="brand-front">
      <span class="brand-mark"></span>
      <div class="brand-text">
        <p class="brand-name">The Larchmont Fitters</p>
        <p class="brand-tagline">Built Square and True</p>
      </div>
    </div>
    <address class="address">
      Harrow Court, 42 Mill Lane<br>
      London N4 7QT
    </address>
    <ul class="contacts">
      <li>
        <svg viewBox="0 0 10 10"><path d="M2 1 L4 3 L3 4.5 Q4.5 6.5 5.5 7 L7 6 L9 8 L7.5 9.3 Q3 8 0.8 2.5 Z"/></svg>
        0207 555 0148
      </li>
      <li>
        <svg viewBox="0 0 10 10"><rect x="0.8" y="2" width="8.4" height="6"/><path d="M0.8 2 L5 5.5 L9.2 2"/></svg>
        info@glimmerbayinteriors.com
      </li>
      <li>
        <svg viewBox="0 0 10 10"><circle cx="5" cy="5" r="4"/><path d="M1 5 H9 M5 1 Q2.5 5 5 9 M5 1 Q7.5 5 5 9"/></svg>
        www.glimmerbayinteriors.com
      </li>
    </ul>
  </section>

  <section class="card card-back" aria-label="Card back">
    <div class="brand-back">
      <span class="brand-mark"></span>
      <div class="brand-text">
        <p class="brand-name">THE LARCHMONT FITTERS</p>
        <p class="brand-tagline">Built Square and True</p>
      </div>
    </div>
    <p class="back-url">www.<strong>glimmerbayinteriors</strong>.com</p>
  </section>
</body>
</html>
```